Appointment card needed

I need an appointment card that has a teal colour theme which will be targeted at women 40 plus. Ideally I would like something that reflects the business name. The business primarily offers a non invasive anti ageing facials and massages

Industry/Entity Type

Business

Contact Information for Business Card

FernDuchess
27 Lindale Rd, Marwick
08 9371 5820

Logo styles of interest
Wordmark Logo

```html
<!DOCTYPE html>
<html lang="en">
<head>
<meta charset="utf-8">
<title>Evergrace Appointment Card</title>
<link rel="stylesheet" href="https://fonts.googleapis.com/css2?family=Josefin+Sans:wght@300&family=Dancing+Script:wght@500&family=PT+Sans+Narrow&display=swap">
<style>
  :root {
    --canvas-bg: #e9ecec;
    --card-white: #ffffff;
    --teal: #12847f;
    --teal-deep: #0b6e6a;
    --ink: #2b2b2b;
    --ink-soft: #3a3a3a;
    --band-text: #ffffff;
  }
  html, body {
    margin: 0;
    padding: 0;
    width: 1200px;
    height: 864px;
    overflow: hidden;
    background: var(--canvas-bg);
  }
  .canvas {
    position: relative;
    width: 1200px;
    height: 864px;
  }
  .card {
    position: absolute;
    left: 150px;
    top: 175px;
    width: 900px;
    height: 514px;
    background: var(--card-white);
    box-shadow: 0 10px 30px rgba(0,0,0,0.18);
    overflow: hidden;
  }
  .corner-accent {
    position: absolute;
    top: 0;
    right: 0;
    width: 150px;
    height: 80px;
  }
  .brand {
    position: absolute;
    left: 120px;
    top: 120px;
    display: flex;
    align-items: center;
    gap: 28px;
  }
  .brand-dot {
    width: 120px;
    height: 120px;
    border-radius: 50%;
    background: var(--teal);
    flex: none;
  }
  .brand-text {
    display: flex;
    flex-direction: column;
  }
  .brand-name {
    font-family: "Josefin Sans", sans-serif;
    font-weight: 300;
    font-size: 84px;
    line-height: 1;
    color: var(--ink);
    letter-spacing: 1px;
  }
  .tagline {
    font-family: "Dancing Script", cursive;
    font-weight: 500;
    font-size: 42px;
    color: var(--ink-soft);
    margin-top: 6px;
    margin-left: 4px;
  }
  .contact-band {
    position: absolute;
    left: 0;
    bottom: 0;
    width: 100%;
    height: 150px;
    background: linear-gradient(90deg, var(--teal-deep), var(--teal));
    box-sizing: border-box;
    padding: 30px 0 0 120px;
  }
  .contact-line {
    font-family: "PT Sans Narrow", sans-serif;
    font-size: 38px;
    line-height: 1.25;
    color: var(--band-text);
    margin: 0;
  }
</style>
</head>
<body>
<main class="canvas">
  <section class="card" aria-label="Appointment card">
    <svg class="corner-accent" viewBox="0 0 150 80" aria-hidden="true">
      <polygon points="0,0 150,0 150,80" fill="var(--teal)"/>
    </svg>

    <div class="brand">
      <div class="brand-dot" aria-hidden="true"></div>
      <div class="brand-text">
        <span class="brand-name">Evergrace</span>
        <span class="tagline">Facials and massages</span>
      </div>
    </div>

    <div class="contact-band">
      <p class="contact-line">FernDuchess 27 Lindale Rd, Marwick</p>
      <p class="contact-line">08 9371 5820</p>
    </div>
  </section>
</main>
</body>
</html>
```